Gemstones e-commerce web-site needs a new template/style

We would like to highlight some of our more exclusive product (gemstones) in a new signature template that has its own style, fonts and colors. The new template would allow for larger and more detailed images. e.g. Tovelcrest.com. The design should account for different sized mobile devices. Current site is http://www.quarlinstonesusa.example

Industry/Entity Type

Product

Number of Pages Required

2 page

```html
<!DOCTYPE html>
<html lang="en">
<head>
<meta charset="utf-8">
<title>QuarlinStonesUSA – Home</title>
<link href="https://fonts.googleapis.com/css2?family=Roboto:wght@300;400;500&display=swap" rel="stylesheet">
<style>
:root{
  --outer:#d9d9d9;
  --page:#ffffff;
  --header-bg:#ececec;
  --nav:#4a4a4a;
  --ink:#333333;
  --muted:#777777;
  --light:#9a9a9a;
  --rule:#e3e3e3;
  --price:#5bc0de;
  --green:#7cb342;
  --cart:#a5c83c;
  --sale:#6ccbe0;
  --hero:#efeff3;
  --footer:#3a3a3a;
  --footer-text:#bdbdbd;
  --footer-bottom:#2f2f2f;
}
*{margin:0;padding:0;box-sizing:border-box}
html,body{width:960px;height:1200px;overflow:hidden}
body{background:var(--outer);font-family:'Roboto',Arial,sans-serif;font-weight:400;color:var(--ink);position:relative}
h1,h2,h3,h4{font-weight:400}
.page{position:absolute;left:143px;top:0;width:661px;height:1200px;background:var(--page);overflow:hidden}
.abs{position:absolute}
ul{list-style:none}

/* header */
.header{position:absolute;left:0;top:0;width:661px;height:102px;background:var(--header-bg)}
.topbar{font-size:5.5px;color:var(--muted);top:7px}
.topbar span{margin-right:8px}
.logo{left:63px;top:38px;display:flex;align-items:center;gap:4px}
.logo-mark{width:9px;height:12px;background:var(--green)}
.logo-name{font-size:14px;font-weight:500;color:#3d3d3d;letter-spacing:-.3px}
.tagline{left:81px;top:59px;font-size:7px;color:#555}
.search{left:270px;top:44px;width:125px;height:14px;background:#fff;border:1px solid #dcdcdc;font-size:5px;color:#999;padding:4px 7px}
.search svg{position:absolute;right:4px;top:2px}
.support{left:438px;top:43px;font-size:6px;color:#555;line-height:7px;padding-left:8px}
.support small{color:#999;font-size:5.5px}
.support svg{position:absolute;left:0;top:1px}
.cart-box{left:545px;top:44px;width:26px;height:20px;background:#fff;border:1px solid #e0e0e0}
.cart-badge{left:563px;top:36px;width:13px;height:13px;border-radius:50%;background:#27a844;color:#fff;font-size:6px;text-align:center;line-height:13px}
.nav{left:63px;top:80px;width:515px;height:22px;background:var(--nav);display:flex;align-items:center;padding-left:14px}
.nav a{color:#fff;font-size:6.5px;text-decoration:none;margin-right:14px}

/* sidebar */
.box{position:absolute;left:63px;width:119px;background:#fff;border:1px solid #efefef}
.box-title{font-size:8.5px;color:#333;padding:10px 0 0 13px}
.cat-list{margin:6px 12px 0 13px}
.cat-list li{display:flex;justify-content:space-between;font-size:5.5px;color:var(--muted);height:13.6px;line-height:13px;border-bottom:1px solid var(--rule)}
.promo{background:#f6f6f6;text-align:center}
.promo h3{font-weight:300;font-size:9.5px;margin-top:10px}
.promo .sub{font-size:5.5px;color:var(--muted);margin:12px 20px 0;line-height:7px;border-top:1px solid var(--rule);padding-top:6px}
.photo{position:absolute}
.btn{position:absolute;background:#fff;border:1px solid #ddd;font-size:6px;color:#555;text-align:center}
.dots{position:absolute;display:flex;gap:4px}
.dots i{width:5px;height:5px;border-radius:50%;background:#ddd;display:block}
.dots i.on{background:var(--price)}
.special{position:absolute;left:13px;display:flex;gap:8px}
.special .thumb{width:35px;height:37px}
.special p{font-size:6px;color:#333;margin-top:2px}
.special b{display:block;font-weight:400;color:var(--price);font-size:6.5px;margin-top:2px}

/* hero */
.hero{left:196px;top:108px;width:382px;height:165px;background:var(--hero)}
.hero h1{position:absolute;left:218px;top:10px;font-weight:300;font-size:23px;line-height:22px;color:#444;letter-spacing:.5px}
.hero .rule{position:absolute;left:218px;top:66px;width:133px;height:1px;background:#ddd}
.hero .from{position:absolute;left:219px;top:72px;font-size:12px;font-weight:300;color:#bbb}
.hero .from span{color:var(--price);font-size:18px}
.hero .desc{position:absolute;left:219px;top:105px;font-size:6px;color:var(--muted);line-height:8px;width:135px}
.deal{left:196px;top:278px;width:382px;height:40px;background:var(--green)}
.deal p{position:absolute;left:37px;top:11px;color:#fff;font-size:15.5px;font-weight:300}
.deal .btn{left:307px;top:12px;width:65px;height:17px;line-height:15px;border:none;color:#555}

/* products */
.sec-title{position:absolute;left:196px;font-weight:300;font-size:15.5px;color:#333}
.arrows{position:absolute;left:557px;display:flex;gap:7px}
.card{position:absolute;width:118px;border:1px solid #eee;background:#fff}
.card .img{height:152px}
.card .name{font-size:6px;margin:10px 0 0 8px;color:#333}
.card .price{font-size:5.5px;margin:3px 0 0 8px;color:#555}
.card .price b{font-weight:400;color:var(--price);font-size:8.5px}
.card .cart{position:absolute;right:7px;top:160px;width:15px;height:15px;border-radius:50%;background:var(--cart)}
.card .cart svg{position:absolute;left:3px;top:3.5px}
.stars{font-size:6px;margin:6px 0 0 16px;color:#ccc}
.stars b{color:var(--cart);font-weight:400}
.links{font-size:5px;margin:8px 0 0 8px;color:#333}
.links span{color:#aaa}
.sale{position:absolute;right:4px;top:4px;background:var(--sale);color:#fff;font-size:5.5px;padding:2px 4px}

/* partners */
.partners{left:0;top:888px;width:661px;height:118px;background:var(--header-bg)}
.badge{position:absolute;top:30px;height:50px;background:#fff;border:1px solid #e6e6e6}

/* footer */
.footer{left:0;top:1006px;width:661px;height:174px;background:var(--footer)}
.connect{position:absolute;left:63px;top:8px;font-size:5.5px;color:#ddd;display:flex;align-items:center;gap:12px}
.connect i{width:7px;height:7px;border-radius:50%;background:#8a8a8a;display:block}
.footer .sep{position:absolute;left:0;top:22px;width:661px;height:1px;background:#2e2e2e}
.fcol{position:absolute;top:39px;color:var(--footer-text);font-size:5.5px}
.fcol h4{font-weight:400;font-size:8px;color:#e0e0e0;margin-bottom:9px}
.fcol li{height:13.2px}
.fcol li:before{content:"›";color:var(--green);margin-right:4px}
.fcol p{line-height:13.2px}
.fcol .txt{line-height:8px;width:120px}
.email{margin-top:6px;width:120px;height:15px;border:1px solid #555;padding:4px 6px;color:#999}
.submit{display:inline-block;background:var(--cart);color:#fff;padding:3px 7px;margin-top:10px;vertical-align:top}
.note{display:inline-block;width:78px;margin:11px 0 0 4px;line-height:6px;font-size:5px}
.bottom{left:0;top:1180px;width:661px;height:20px;background:var(--footer-bottom)}
.bottom p{position:absolute;left:63px;top:7px;font-size:5px;color:#bbb}
.pay{position:absolute;top:5px;width:14px;height:9px;background:#e8e8e8;border-radius:1px}
</style>
</head>
<body>
<div class="page">

  <header class="header">
    <div class="abs topbar" style="left:63px"><span>• Account</span><span>• Checkout</span><span>• Store</span></div>
    <div class="abs topbar" style="left:268px">
      <svg width="5" height="6" viewBox="0 0 10 12" style="vertical-align:-1px"><path d="M5 0a4 4 0 0 1 4 4c0 3-4 8-4 8S1 7 1 4a4 4 0 0 1 4-4z" fill="#888"/></svg>
      4471 Larkspur Avenue Westmoor</div>
    <div class="abs topbar" style="left:477px">Language: <b style="font-weight:400;color:#333">English ⌄</b></div>
    <div class="abs topbar" style="left:537px">Currency: <b style="font-weight:400;color:#333">USD ⌄</b></div>

    <div class="abs logo"><span class="logo-mark"></span><span class="logo-name">QuarlinStonesUSA</span></div>
    <div class="abs tagline">Stones of Rare Light</div>

    <div class="abs search">Search entire store here...
      <svg width="9" height="9" viewBox="0 0 10 10"><circle cx="4" cy="4" r="3" fill="none" stroke="#999" stroke-width="1"/><path d="M6.3 6.3 9 9" stroke="#999" stroke-width="1"/></svg>
    </div>
    <div class="abs support">
      <svg width="5" height="9" viewBox="0 0 6 10"><path d="M1 0h2l1 3-1.5 1c.3 1.5 1 2.5 1.5 3L5 6l1 2-1 2C2 10 0 6 0 2z" fill="var(--green)"/></svg>
      Customer Support<br><small>Call: + 0555 201 874</small></div>
    <div class="abs cart-box">
      <svg width="12" height="10" viewBox="0 0 12 10" style="position:absolute;left:7px;top:5px"><path d="M0 1h2l1.5 5h6L11 2.5H3" fill="none" stroke="#999" stroke-width="1"/><circle cx="4.5" cy="8.5" r="1" fill="#999"/><circle cx="8.5" cy="8.5" r="1" fill="#999"/></svg>
    </div>
    <div class="abs cart-badge">12</div>

    <nav class="abs nav"><a>HOME</a><a>ABOUT</a><a>NEW PRODUCT</a><a>NEWS</a><a>CONTACT US</a></nav>
  </header>

  <aside>
    <section class="box" style="top:108px;height:144px">
      <h3 class="box-title">Shop categories</h3>
      <ul class="cat-list">
        <li><span>Gemstones</span><span>(8)</span></li>
        <li><span>Shows</span><span>(10)</span></li>
        <li><span>Special Gemstones</span><span>(3)</span></li>
        <li><span>Carvings</span><span>(5)</span></li>
        <li><span>Beads</span><span>(7)</span></li>
        <li><span>Gold Jewelry</span><span>(17)</span></li>
        <li><span>Silver Jewelery</span><span>(7)</span></li>
      </ul>
    </section>

    <section class="box promo" style="top:270px;height:216px">
      <h3>New Gene Jacket</h3>
      <p class="sub">Fincidunt eu, mattis a libero.<br>Pelletequ</p>
      <div class="photo" role="img" aria-label="Star-patterned ceramic bowls stacked on a striped cloth with a spoon" style="left:4px;top:54px;width:110px;height:122px;background:linear-gradient(160deg,#c9c9c9,#8a4a4a 55%,#6f86b0)"></div>
      <div class="btn" style="left:31px;top:167px;width:62px;height:17px;line-height:16px">CHECK IT OUT</div>
      <div class="dots" style="left:47px;top:204px"><i class="on"></i><i></i><i></i></div>
    </section>

    <section class="box" style="top:496px;height:214px">
      <h3 class="box-title">Specials</h3>
      <div class="special" style="top:26px"><div class="thumb" role="img" aria-label="Pastel teacups" style="background:linear-gradient(135deg,#e6e6de,#9cc8b0)"></div><p>New Gene Jacket<b>$124.00</b></p></div>
      <div class="special" style="top:72px"><div class="thumb" role="img" aria-label="White ceramic teapot" style="background:linear-gradient(135deg,#f0f0ee,#cfcfca)"></div><p>New Gene Jacket<b>$124.00</b></p></div>
      <div class="special" style="top:118px"><div class="thumb" role="img" aria-label="Patterned teacup set" style="background:linear-gradient(135deg,#eeeeea,#d7b86a)"></div><p>New Gene Jacket<b>$124.00</b></p></div>
      <div class="special" style="top:164px"><div class="thumb" role="img" aria-label="Stacked colourful bowls" style="background:linear-gradient(135deg,#ecece8,#4aa9b8)"></div><p>New Gene Jacket<b>$124.00</b></p></div>
    </section>

    <section class="abs" role="img" aria-label="Pine branches on a wooden table behind the final sale offer" style="left:62px;top:730px;width:120px;height:104px;background:linear-gradient(160deg,#55644f,#8c948a 60%,#a7aba3)">
      <p class="abs" style="left:0;width:120px;top:18px;text-align:center;color:#fff;font-size:20px;font-weight:500">50% OFF</p>
      <p class="abs" style="left:0;width:120px;top:44px;text-align:center;color:#c6e77a;font-size:7px;font-weight:500">FINAL SALE</p>
      <div class="btn" style="left:29px;top:62px;width:62px;height:17px;line-height:16px;border:none">SHOP NOW!</div>
      <div class="dots" style="left:49px;top:89px"><i class="on"></i><i style="background:#fff"></i><i style="background:#fff"></i></div>
    </section>
  </aside>

  <section class="abs hero">
    <div class="abs" role="img" aria-label="Silver ring set with a large cushion-cut purple amethyst and a halo of small diamonds" style="left:36px;top:14px;width:124px;height:140px;background:radial-gradient(ellipse at 55% 35%,#7b3fc4 0,#5a2a99 28%,#c9c9cf 48%,var(--hero) 72%)"></div>
    <h1>Jeweler<br>Collection</h1>
    <div class="rule"></div>
    <p class="from">from <span>$9.99</span></p>
    <p class="desc">Praesent augue arcu, ornare ut tincidunt eu, mattis a libero. Pellentesquehabitant.</p>
    <div class="btn" style="left:219px;top:126px;width:80px;height:18px;line-height:17px;background:transparent">VIEW COLLECTION</div>
  </section>

  <section class="abs deal">
    <svg class="abs" style="left:11px;top:5px" width="18" height="30" viewBox="0 0 18 30"><path d="M9 1c2 0 3 2 2 4" fill="none" stroke="#fff" stroke-width="1.3"/><path d="M3 9 9 5l6 4v17H3z" fill="none" stroke="#fff" stroke-width="1.5"/><circle cx="9" cy="10" r="1.3" fill="#fff"/><text x="9" y="22" font-size="8" fill="#fff" text-anchor="middle" font-family="Roboto,sans-serif">$</text></svg>
    <p>Get 20% discount on orders over $300</p>
    <div class="btn">VIEW DETAILS</div>
  </section>

  <h2 class="sec-title" style="top:329px">Top Sellers</h2>
  <div class="arrows" style="top:335px">
    <svg width="6" height="8"><path d="M5 1 2 4l3 3" fill="none" stroke="var(--cart)" stroke-width="1.2"/></svg>
    <svg width="6" height="8"><path d="M1 1l3 3-3 3" fill="none" stroke="#444" stroke-width="1.2"/></svg>
  </div>

  <article class="card" style="left:196px;top:358px;height:212px">
    <div class="img" role="img" aria-label="Pair of purple amethyst earrings with diamond halos" style="background:radial-gradient(circle at 50% 55%,#6b2fb0 0,#9a8aa8 30%,#efefef 60%)"></div>
    <p class="name">New Gene Jacket</p>
    <p class="price">Starting at: <b>$124.00</b></p>
    <div class="cart"><svg width="9" height="8" viewBox="0 0 12 10"><path d="M0 1h2l1.5 5h6L11 2.5H3z" fill="#fff"/><circle cx="4.5" cy="8.5" r="1.2" fill="#fff"/><circle cx="8.5" cy="8.5" r="1.2" fill="#fff"/></svg></div>
    <p class="stars"><b>★ ★</b> ★ ★ <span style="font-size:5px;color:#999;margin-left:3px">(14)</span></p>
    <p class="links">ADD TO WISHLIST &nbsp;| &nbsp;<span>ADD TO COMPARE</span></p>
  </article>

  <article class="card" style="left:328px;top:358px;height:191px">
    <div class="img" role="img" aria-label="Silver drop earrings and pendant with pink ruby stones" style="background:radial-gradient(circle at 50% 55%,#d8c7cb 0,#ececec 45%,#f3f3f3 70%)"></div>
    <p class="name">New Gene Jacket</p>
    <p class="price">Starting at: <b>$124.00</b></p>
    <div class="cart"><svg width="9" height="8" viewBox="0 0 12 10"><path d="M0 1h2l1.5 5h6L11 2.5H3z" fill="#fff"/><circle cx="4.5" cy="8.5" r="1.2" fill="#fff"/><circle cx="8.5" cy="8.5" r="1.2" fill="#fff"/></svg></div>
  </article>

  <article class="card" style="left:460px;top:358px;height:191px">
    <div class="img" role="img" aria-label="Ornate gold pendant set with an orange-red gemstone" style="background:radial-gradient(circle at 50% 50%,#c0392b 0,#e0b43a 22%,#ede8dc 50%)"></div>
    <span class="sale">SALE!</span>
    <p class="name">New Gene Jacket</p>
    <p class="price">Starting at: <b>$124.00</b></p>
    <div class="cart"><svg width="9" height="8" viewBox="0 0 12 10"><path d="M0 1h2l1.5 5h6L11 2.5H3z" fill="#fff"/><circle cx="4.5" cy="8.5" r="1.2" fill="#fff"/><circle cx="8.5" cy="8.5" r="1.2" fill="#fff"/></svg></div>
  </article>

  <h2 class="sec-title" style="top:585px">New Products</h2>
  <div class="arrows" style="top:591px">
    <svg width="6" height="8"><path d="M5 1 2 4l3 3" fill="none" stroke="var(--cart)" stroke-width="1.2"/></svg>
    <svg width="6" height="8"><path d="M1 1l3 3-3 3" fill="none" stroke="#444" stroke-width="1.2"/></svg>
  </div>

  <article class="card" style="left:196px;top:614px;height:190px">
    <div class="img" role="img" aria-label="Gold and silver rings with green and yellow gemstones on a dark surface" style="background:linear-gradient(150deg,#2a2a2a,#6b6250 50%,#b99a4a 75%,#1c1c1c)"></div>
    <p class="name">New Gene Jacket</p>
    <p class="price">Starting at: <b>$124.00</b></p>
    <div class="cart"><svg width="9" height="8" viewBox="0 0 12 10"><path d="M0 1h2l1.5 5h6L11 2.5H3z" fill="#fff"/><circle cx="4.5" cy="8.5" r="1.2" fill="#fff"/><circle cx="8.5" cy="8.5" r="1.2" fill="#fff"/></svg></div>
  </article>

  <article class="card" style="left:328px;top:614px;height:190px">
    <div class="img" role="img" aria-label="Diamond engagement ring in close-up on black" style="background:radial-gradient(circle at 40% 35%,#e8e8e8 0,#8a8a8a 30%,#2b2b2b 65%,#111 100%)"></div>
    <p class="name">New Gene Jacket</p>
    <p class="price">Starting at: <b>$124.00</b></p>
    <div class="cart"><svg width="9" height="8" viewBox="0 0 12 10"><path d="M0 1h2l1.5 5h6L11 2.5H3z" fill="#fff"/><circle cx="4.5" cy="8.5" r="1.2" fill="#fff"/><circle cx="8.5" cy="8.5" r="1.2" fill="#fff"/></svg></div>
  </article>

  <article class="card" style="left:460px;top:614px;height:190px">
    <div class="img" role="img" aria-label="Engraved gold heart-shaped lockets" style="background:radial-gradient(circle at 50% 50%,#c9a24e 0,#7a5a22 40%,#2e2412 80%)"></div>
    <p class="name">New Gene Jacket</p>
    <p class="price">Starting at: <b>$124.00</b></p>
    <div class="cart"><svg width="9" height="8" viewBox="0 0 12 10"><path d="M0 1h2l1.5 5h6L11 2.5H3z" fill="#fff"/><circle cx="4.5" cy="8.5" r="1.2" fill="#fff"/><circle cx="8.5" cy="8.5" r="1.2" fill="#fff"/></svg></div>
  </article>

  <section class="abs partners" aria-label="Memberships">
    <div class="badge" style="left:65px;width:49px"></div>
    <div class="badge" style="left:148px;width:95px"></div>
    <div class="badge" style="left:273px;width:100px"></div>
    <div class="badge" style="left:403px;width:95px"></div>
    <div class="arrows" style="left:559px;top:33px">
      <svg width="6" height="8"><path d="M5 1 2 4l3 3" fill="none" stroke="var(--cart)" stroke-width="1.2"/></svg>
      <svg width="6" height="8"><path d="M1 1l3 3-3 3" fill="none" stroke="#444" stroke-width="1.2"/></svg>
    </div>
  </section>

  <footer class="abs footer">
    <div class="connect">Let's Connect:
      <i style="margin-left:8px"></i><i></i><i></i><i></i><i></i><i></i><i></i><i></i><i></i><i></i><i></i><i></i><i></i>
    </div>
    <div class="sep"></div>

    <div class="fcol" style="left:63px">
      <h4>The Company</h4>
      <ul><li>About QuarlinStonesUSA</li><li>Contact Us</li><li>FAQ's</li><li>Testimonials</li><li>How to Order</li><li>Terms &amp; Condition</li></ul>
    </div>
    <div class="fcol" style="left:195px">
      <h4>The Services</h4>
      <ul><li>Policies</li><li>Privacy Policy</li><li>Site Map</li><li>Contact us</li><li>Become a Partner</li><li>About</li></ul>
    </div>
    <div class="fcol" style="left:327px">
      <h4>Contacts Us</h4>
      <p>18 Orchard Lane, Suite 310</p>
      <p>Westmoor , Calden 20417</p>
      <p>Phone: +(555) 014-2290</p>
      <p>Email: hello@quarlinstones.example</p>
    </div>
    <div class="fcol" style="left:459px">
      <h4>Subscribe To Our Newsletter</h4>
      <p class="txt">Praesent augue arcu, ornare ut tincidunt eu, mattis a libero. Pellentesquehabitant morbi tristique senectus et netus</p>
      <div class="email">Enter your Email</div>
      <span class="submit">Submit</span><span class="note">* Praesent augue arcu, ornare ut tincidunt eu, mattis</span>
    </div>
  </footer>

  <div class="abs bottom">
    <p>copyright 2013 - Lumen Theme</p>
    <span class="pay" style="left:489px"></span>
    <span class="pay" style="left:507px"></span>
    <span class="pay" style="left:525px"></span>
    <span class="pay" style="left:543px"></span>
    <span class="pay" style="left:561px"></span>
  </div>

</div>
</body>
</html>
```